Skill Up Salary Up

Full Page
7.5 w x 10 h / 8 w x 10.75 h + .25" bleed
Full-Page Career Course Ad
Project Overview
• Goal: Create a visually attractive, modern, and uncluttered full-page magazine advertisement to list available career courses.
• Tone: Creative, professional, and attention-grabbing to prevent the reader from turning the page. The final design must prioritize readability.

Content Requirements
1. Header/Headline: Must be the primary focus. And grab peoples attention
2. Course Listing: A clear, well-organized list of the career courses.
________________________________________
Design & Aesthetic Directives
1. Layout & Readability (Crucial)
• The final ad must not look crowded or busy.
• Prioritize white space to make the text "breathe" and ensure the course list is easy to scan and read.
• Use a modern, clean, and professional typeface (font choice is critical for the aesthetic).
2. Visual Style
• Aim for a creative, modern, and fresh look. Avoid outdated or generic stock imagery/layouts.
3. Imagery/Graphic Element (Artist's Choice)
You have creative freedom regarding the main graphic element.
• Option A (Photography): Use a photo of a white male American with a collared shirt. The imagery should convey success, focus, or professional development.
• Option B (Vector/Illustration): Use a modern vector graphic, illustration, or abstract design. This could be used to symbolize growth, connection, or a career path.
The choice of graphic element is yours, but it must support the overall modern and uncrowded aesthetic.

Requirements
Must have
• Partial listing .. is part of the Harbor Lantern Course

```html
<!DOCTYPE html>
<html lang="en">
<head>
<meta charset="utf-8">
<title>Skill Up, Salary Up – Upcoming HLC Courses</title>
<link href="https://fonts.googleapis.com/css2?family=Nunito:wght@800;900&family=Nunito+Sans:wght@900&family=Jost:wght@300;400&display=swap" rel="stylesheet">
<style>
  :root {
    --cream: #fdf6ea;
    --teal: #00a0a5;
    --teal-deep: #0d4f63;
    --coral: #f4564a;
    --blob: #ebebeb;
    --ink: #1a1a1a;
    --white: #ffffff;
  }
  * { margin: 0; padding: 0; box-sizing: border-box; }
  html, body { width: 900px; height: 1200px; overflow: hidden; background: var(--white); }
  .ad { position: relative; width: 900px; height: 1200px; overflow: hidden; background: var(--white); color: var(--ink); font-family: "Jost", sans-serif; }
  .backdrop { position: absolute; inset: 0; }
  .abs { position: absolute; white-space: nowrap; }

  .tagline { left: 129px; top: 100px; font-family: "Nunito Sans", sans-serif; font-weight: 900; font-size: 33px; color: var(--teal-deep); letter-spacing: .3px; }
  .headline { left: 70px; top: 138px; font-family: "Nunito Sans", sans-serif; font-weight: 900; font-size: 59px; letter-spacing: -.5px; line-height: 1; }
  .audience { top: 206px; font-size: 25px; font-weight: 300; letter-spacing: -.3px; }

  .course-title { font-family: "Nunito", sans-serif; font-weight: 900; font-size: 26px; line-height: 1; }
  .course-sub { font-family: "Nunito", sans-serif; font-weight: 900; font-size: 17.5px; line-height: 1.15; }
  .course-item { font-size: 17px; font-weight: 300; line-height: 1; }
  .bullet { font-family: "Nunito", sans-serif; font-weight: 900; font-size: 15px; margin-right: 3px; }
  .course-item .bullet + .bullet { margin-left: 0; }
  .badge { position: absolute; width: 101px; height: 38px; border-radius: 8px; background: var(--coral); color: var(--white); font-family: "Nunito", sans-serif; font-weight: 900; font-size: 12.5px; line-height: 13.5px; display: flex; flex-direction: column; align-items: center; justify-content: center; text-align: center; }

  .portrait { position: absolute; left: 540px; top: 560px; width: 340px; height: 640px; }
</style>
</head>
<body>
<main class="ad">
  <svg class="backdrop" width="900" height="1200" viewBox="0 0 900 1200">
    <rect class="header-band" width="900" height="262" fill="var(--cream)"/>
    <path class="header-swoosh" d="M488 0 C520 60 580 100 650 98 C730 96 800 70 900 112 L900 0 Z" fill="var(--teal)"/>
    <path class="header-rule" d="M40 258 L900 258 L900 272 Z" fill="var(--teal)"/>

    <path class="section-blob" d="M120 290 C200 270 240 320 300 330 C380 345 420 380 422 440 C424 520 330 570 250 550 C170 530 90 520 70 440 C55 370 60 310 120 290 Z" fill="var(--blob)"/>
    <path class="section-blob" d="M560 300 C640 290 700 310 770 300 C830 300 835 380 810 420 C780 470 740 480 730 520 C700 570 620 570 560 540 C500 500 490 440 495 380 C500 330 520 305 560 300 Z" fill="var(--blob)"/>
    <path class="section-blob" d="M130 560 C220 545 300 580 350 620 C390 660 390 740 340 770 C290 790 200 780 140 750 C70 710 45 640 80 590 C95 570 110 563 130 560 Z" fill="var(--blob)"/>
    <path class="section-blob" d="M150 780 C240 765 360 790 430 810 C460 840 440 900 400 935 C340 960 220 950 140 935 C80 920 65 870 80 820 C95 795 120 785 150 780 Z" fill="var(--blob)"/>
    <path class="section-blob" d="M180 975 C280 960 360 995 430 1010 C480 1025 480 1080 440 1100 C370 1125 250 1125 170 1118 C95 1110 60 1070 75 1030 C90 995 130 982 180 975 Z" fill="var(--blob)"/>

    <path class="portrait-blob" d="M900 612 C810 585 700 600 620 650 C560 690 545 760 550 820 C556 900 555 1000 565 1080 C572 1140 580 1175 590 1200 L900 1200 Z" fill="var(--teal)"/>

    <g class="dot-grid" fill="var(--teal)">
      <circle cx="445" cy="610" r="3.6"/><circle cx="463" cy="610" r="3.6"/><circle cx="481" cy="610" r="3.6"/><circle cx="498" cy="610" r="3.6"/><circle cx="516" cy="610" r="3.6"/><circle cx="534" cy="610" r="3.6"/>
      <circle cx="445" cy="630" r="3.6"/><circle cx="463" cy="630" r="3.6"/><circle cx="481" cy="630" r="3.6"/><circle cx="498" cy="630" r="3.6"/><circle cx="516" cy="630" r="3.6"/><circle cx="534" cy="630" r="3.6"/>
      <circle cx="445" cy="651" r="3.6"/><circle cx="463" cy="651" r="3.6"/><circle cx="481" cy="651" r="3.6"/><circle cx="498" cy="651" r="3.6"/><circle cx="516" cy="651" r="3.6"/><circle cx="534" cy="651" r="3.6"/>
      <circle cx="445" cy="671" r="3.6"/><circle cx="463" cy="671" r="3.6"/><circle cx="481" cy="671" r="3.6"/><circle cx="498" cy="671" r="3.6"/><circle cx="516" cy="671" r="3.6"/><circle cx="534" cy="671" r="3.6"/>
    </g>
    <g class="dot-column" fill="var(--teal)">
      <circle cx="525" cy="1034" r="3.6"/><circle cx="545" cy="1034" r="3.6"/>
      <circle cx="525" cy="1052" r="3.6"/><circle cx="545" cy="1052" r="3.6"/>
      <circle cx="525" cy="1070" r="3.6"/><circle cx="545" cy="1070" r="3.6"/>
      <circle cx="525" cy="1087" r="3.6"/><circle cx="545" cy="1087" r="3.6"/>
      <circle cx="525" cy="1105" r="3.6"/><circle cx="545" cy="1105" r="3.6"/>
      <circle cx="525" cy="1122" r="3.6"/><circle cx="545" cy="1122" r="3.6"/>
    </g>
  </svg>

  <div class="abs tagline">SKILL UP, SALARY UP</div>
  <h1 class="abs headline">UPCOMING HLC COURSES</h1>
  <div class="abs audience" style="left:73px">MEN &amp; WOMEN</div>
  <div class="abs audience" style="left:292px">IN-PERSON &amp; REMOTE</div>
  <div class="abs audience" style="left:559px">PARTIAL SCHOLORASHIPS</div>

  <section class="course">
    <h2 class="abs course-title" style="left:77px;top:293px">Harbor Lantern Course</h2>
    <p class="abs course-sub" style="left:78px;top:331px">Business Skills &amp; Knowledge to:</p>
    <p class="abs course-item" style="left:79px;top:366px">» Impress your interviewer</p>
    <p class="abs course-item" style="left:79px;top:393px">» Maximize Income</p>
    <p class="abs course-item" style="left:79px;top:420px">» Start / Run Your Business</p>
    <div class="badge" style="left:291px;top:400px"><span>4-5 MONTHS</span><span>NOV 2025</span></div>
    <p class="abs course-sub" style="left:79px;top:452px">PARTIAL LISTING</p>
    <p class="abs course-item" style="left:79px;top:481px"><span class="bullet">•</span>&nbsp; Computers <span class="bullet">•</span> Marketing <span class="bullet">•</span> Sales <span class="bullet">•</span> Finance</p>
    <p class="abs course-item" style="left:79px;top:501px"><span class="bullet">•</span>&nbsp; Healthcare <span class="bullet">•</span> Business Strategy <span class="bullet">•</span> Communication</p>
    <p class="abs course-item" style="left:79px;top:520px"><span class="bullet">•</span>&nbsp; LedgerLeaf <span class="bullet">•</span> Investments <span class="bullet">•</span> Real Estate <span class="bullet">•</span> Accounting</p>
  </section>

  <section class="course">
    <h2 class="abs course-title" style="left:515px;top:293px">Software, Web &amp; Apps</h2>
    <p class="abs course-sub" style="left:516px;top:331px">#2 Best Tech Job<br>National Career Review 2025</p>
    <p class="abs course-sub" style="left:516px;top:382px">Job Opportunities</p>
    <p class="abs course-item" style="left:518px;top:411px"><span class="bullet">•</span> Computer Programmer</p>
    <p class="abs course-item" style="left:518px;top:438px"><span class="bullet">•</span> Software Developer/Mobile</p>
    <p class="abs course-item" style="left:518px;top:465px"><span class="bullet">•</span> Engineer Developer (Apps</p>
    <p class="abs course-sub" style="left:518px;top:494px">Optional</p>
    <p class="abs course-item" style="left:519px;top:523px"><span class="bullet">•</span> Bachelors in Prog. &amp; Tech</p>
    <div class="badge" style="left:730px;top:500px"><span>NOV 2025</span></div>
  </section>

  <section class="course">
    <h2 class="abs course-title" style="left:77px;top:582px">Bookkeeping LedgerLeaf</h2>
    <p class="abs course-sub" style="left:78px;top:620px">Train for a quality job<br>Manage your own books</p>
    <p class="abs course-item" style="left:80px;top:672px"><span class="bullet">•</span> Finance Management</p>
    <p class="abs course-item" style="left:80px;top:699px"><span class="bullet">•</span> Customer &amp; Vendor Mgmt.</p>
    <p class="abs course-item" style="left:80px;top:726px"><span class="bullet">•</span> Advanced Tools</p>
    <div class="badge" style="left:305px;top:675px"><span>5 WEEKS</span><span>NOV 2025</span></div>
  </section>

  <section class="course">
    <h2 class="abs course-title" style="left:77px;top:788px">IT Desktop &amp; Networking Support</h2>
    <p class="abs course-sub" style="left:79px;top:826px">#2 Best Job<br>National Career Review 2025</p>
    <p class="abs course-sub" style="left:79px;top:878px">Masters IT</p>
    <p class="abs course-item" style="left:80px;top:905px"><span class="bullet">•</span> Panelo OS <span class="bullet">•</span> Networks <span class="bullet">•</span> Servers <span class="bullet">•</span> Cloud</p>
    <div class="badge" style="left:374px;top:846px"><span>7 MONTHS</span><span>NOV 2025</span></div>
  </section>

  <section class="course">
    <h2 class="abs course-title" style="left:77px;top:976px">Deskwise Office - Computers</h2>
    <p class="abs course-sub" style="left:79px;top:1015px">The New Job Prerequisite</p>
    <p class="abs course-item" style="left:80px;top:1048px"><span class="bullet">•</span> Gridcalc <span class="bullet">•</span> Docwrite <span class="bullet">•</span> Mailbox <span class="bullet">•</span> Slidecraft</p>
    <p class="abs course-sub" style="left:81px;top:1077px">Computer lab available to practice</p>
    <div class="badge" style="left:400px;top:1058px"><span>5 WEEKS</span><span>NOV 2025</span></div>
  </section>

  <svg class="portrait" viewBox="0 0 340 640" role="img" aria-label="Photo of a smiling young professional man in a white collared shirt and grey trousers, hands in pockets">
    <defs>
      <linearGradient id="portraitTone" x1="0" y1="0" x2="0" y2="1">
        <stop offset="0" stop-color="#e9e4df"/>
        <stop offset="1" stop-color="#d8d8d8"/>
      </linearGradient>
    </defs>
    <path d="M115 0 C160 -8 210 10 215 60 C220 110 200 150 190 175 L260 200 C300 215 305 300 300 400 C296 470 290 560 290 640 L70 640 C70 560 45 470 40 400 C35 300 45 215 95 195 L120 175 C105 140 90 90 95 50 C98 20 105 5 115 0 Z" fill="url(#portraitTone)"/>
  </svg>
</main>
</body>
</html>
```